Wine Label for a wine from Tuscany, Italy

We need a wine label for a white and red wine, can be the same label or can be somewhat differentiated with any variation you feel would be good.. These two wines come from Tuscany, Italy. Wine labels from Tuscany Italy tend to be traditional. We are open to traditional looking labels but also more modern, eye catching too. We want to convey a sense of elegance, importance, great wine. I am attaching some examples of labels we like from Tuscany, also a label that was designed for us recently by one of you, which we LOVE. No wine glasses, wine bottles or grapes featured on the label please. We tend to like the white background. No blue please.

Target Market(s)

More women than men purchase wine, but it needs to appeal to both sexes.

Requirements
Must have
• Wine Name: Casa Morel or Casa morel
• Type/Varletal: Rosso Toscano (White is Vermentino)
• Vintage (year): 2018
• That is all the text we want on the label, thanks
Nice to have
• Clean, something that makes someone want to grab this wine bottle off the shelf!
Should not have
• Images of Wine glass, wine bottles, grapes
• Do not use the color blue please.

```html
<!DOCTYPE html>
<html lang="en">
<head>
<meta charset="utf-8">
<title>Casa Morel — Wine Labels</title>
<link rel="stylesheet" href="https://fonts.googleapis.com/css2?family=Bodoni+Moda:wght@500&family=Josefin+Sans:wght@400&display=swap">
<style>
  :root {
    --backdrop: #333333;
    --label-paper: #f3f3f3;
    --ink: #2e2e2e;
    --mark-light: #f5f5f5;
    --vermentino-gold: #b39a52;
    --rosso-red: #c2262e;
  }
  * { margin: 0; padding: 0; box-sizing: border-box; }
  html, body {
    width: 1200px;
    height: 917px;
    overflow: hidden;
    background: var(--backdrop);
  }
  .board {
    position: relative;
    width: 1200px;
    height: 917px;
  }
  .brand-name {
    font-family: "Bodoni Moda", "Didot", serif;
    font-weight: 500;
    line-height: 0.92;
    letter-spacing: 0.01em;
  }
  .signature {
    position: absolute;
    left: 66px;
    top: 72px;
    width: 200px;
    color: var(--mark-light);
    font-size: 64px;
  }
  .label {
    position: absolute;
    left: 66px;
    width: 411px;
    height: 274px;
    background: var(--label-paper);
  }
  .label--vermentino { top: 290px; }
  .label--rosso { top: 616px; }
  .label .brand-name {
    position: absolute;
    left: 34px;
    top: 38px;
    color: var(--ink);
    font-size: 96px;
  }
  .varietal {
    position: absolute;
    left: 282px;
    top: 207px;
    font-family: "Josefin Sans", "Helvetica Neue", sans-serif;
    font-size: 13px;
    letter-spacing: 0.02em;
    line-height: 1.4;
  }
  .varietal__name { display: block; }
  .varietal__year {
    display: block;
    color: var(--ink);
    font-size: 12px;
    padding-left: 2px;
  }
  .label--vermentino .varietal__name { color: var(--vermentino-gold); }
  .label--rosso .varietal { left: 256px; }
  .label--rosso .varietal__year { padding-left: 28px; }
  .label--vermentino .varietal__year { padding-left: 28px; }
  .label--rosso .varietal__name { color: var(--rosso-red); }
</style>
</head>
<body>
  <main class="board">
    <div class="signature brand-name">Casa<br>Morel</div>

    <section class="label label--vermentino">
      <div class="brand-name">Casa<br>Morel</div>
      <p class="varietal">
        <span class="varietal__name">VERMENTINO</span>
        <span class="varietal__year">2018</span>
      </p>
    </section>

    <section class="label label--rosso">
      <div class="brand-name">Casa<br>Morel</div>
      <p class="varietal">
        <span class="varietal__name">ROSSO TOSCANO</span>
        <span class="varietal__year">2018</span>
      </p>
    </section>
  </main>
</body>
</html>
```